Cobalto Grande

I want a glossy card on both sides. We sell underwater LED lights for water craft

we sell custom audio enclosures for automobile, boats and atv's.

view our websites for any other pictures you may think are better suited.

Industry/Entity Type

Audio

Contact Information for Business Card

Email address: CobaltoGrande@mailvista.example
Website: www.hullglowtap.example
underwater LED lighting for watercraft
boat drain plug lights
phone number: 555-271-0648

other side of card:
email address the same
website: www.versatilesoundshells.example
speaker enclosures, auto, boat and atv
same phone number

```html
<!DOCTYPE html>
<html lang="en">
<head>
<meta charset="utf-8">
<title>Cobalto Grande – Business Cards</title>
<link href="https://fonts.googleapis.com/css2?family=Pinyon+Script&family=Open+Sans:wght@400;700&display=swap" rel="stylesheet">
<style>
  :root {
    --stage-light: #5a5a5a;
    --stage-dark: #1c1c1c;
    --ink: #ffffff;
    --ring: #3a3a3a;
    --deep-night: #05080c;
    --lagoon: #1b8f93;
    --lagoon-glow: #3fc7c4;
    --dusk-violet: #3a3566;
    --dusk-blue: #1a2348;
    --dusk-plum: #5a4060;
  }
  * { margin: 0; padding: 0; box-sizing: border-box; }
  html, body { width: 1200px; height: 1000px; overflow: hidden; }
  body {
    position: relative;
    background: radial-gradient(ellipse at 50% 50%, var(--stage-light) 0%, #3a3a3a 45%, var(--stage-dark) 100%);
    font-family: "Open Sans", sans-serif;
    color: var(--ink);
  }
  .card {
    position: absolute;
    left: 260px;
    width: 680px;
    overflow: hidden;
    box-shadow: 0 4px 14px rgba(0,0,0,0.55);
  }
  .card--lighting { top: 72px; height: 388px; }
  .card--audio { top: 541px; height: 387px; }

  .card__backdrop { position: absolute; inset: 0; }
  .card--lighting .card__backdrop {
    background:
      radial-gradient(ellipse 60% 45% at 30% 100%, var(--lagoon-glow) 0%, rgba(27,143,147,0.6) 35%, transparent 75%),
      radial-gradient(ellipse 35% 55% at 82% 60%, rgba(120,80,70,0.55) 0%, transparent 70%),
      radial-gradient(ellipse 30% 30% at 10% 25%, rgba(130,150,150,0.35) 0%, transparent 70%),
      linear-gradient(180deg, var(--deep-night) 0%, #0b1c22 60%, var(--lagoon) 100%);
  }
  .card--audio .card__backdrop {
    background:
      radial-gradient(ellipse 50% 40% at 50% 30%, rgba(150,110,130,0.45) 0%, transparent 75%),
      radial-gradient(ellipse 40% 50% at 85% 45%, rgba(110,120,180,0.4) 0%, transparent 75%),
      linear-gradient(180deg, var(--dusk-plum) 0%, var(--dusk-violet) 40%, var(--dusk-blue) 75%, #0d0f22 100%);
  }

  .photo-disc {
    position: absolute;
    border-radius: 50%;
    border: 5px solid var(--ring);
    box-shadow: 0 2px 8px rgba(0,0,0,0.6);
  }
  .photo-disc--night { background: radial-gradient(circle at 50% 60%, #4f7fd8 0%, #1a3570 40%, #050a1c 80%); }
  .photo-disc--sunset { background: linear-gradient(180deg, #27324e 0%, #c08a5a 38%, #1a2c52 50%, #1d6d6b 80%, #0b2a33 100%); }
  .photo-disc--green { background: linear-gradient(180deg, #0b0e18 0%, #233040 40%, #6f8c5a 70%, #c7d25a 100%); }
  .photo-disc--wake { background: radial-gradient(circle at 50% 70%, #4aa0e8 0%, #1a4a90 35%, #050a18 80%); }
  .photo-disc--speaker { background: radial-gradient(circle at 55% 40%, #f2f2f2 0%, #b4b4b4 35%, #4a4a4a 65%, #e8e8e8 90%); }
  .photo-disc--pod { background: radial-gradient(circle at 50% 50%, #2a2a2a 0%, #505050 45%, #f2f2f2 70%); }

  .brand-name {
    position: absolute;
    font-family: "Pinyon Script", cursive;
    font-weight: 400;
    color: var(--ink);
    white-space: nowrap;
    line-height: 1;
  }
  .card--lighting .brand-name { right: 22px; top: 46px; font-size: 64px; }
  .card--audio .brand-name { left: 46px; top: 46px; font-size: 62px; }

  .line {
    position: absolute;
    white-space: nowrap;
    text-align: center;
    transform: translateX(-50%);
    line-height: 1;
  }
  .line--web { font-weight: 700; font-size: 17px; }
  .line--email { font-size: 16px; }
  .line--phone { font-size: 18px; letter-spacing: 1.5px; }
  .line--service { font-size: 21px; }
  .line--heading { font-weight: 700; font-size: 20px; }
  .line--sub { font-size: 20px; }
</style>
</head>
<body>

<section class="card card--lighting">
  <div class="card__backdrop" role="img" aria-label="Night harbour scene with boats glowing under teal underwater lights"></div>

  <div class="photo-disc photo-disc--night" style="left:150px;top:58px;width:120px;height:120px" role="img" aria-label="Boat at night lit by blue underwater light"></div>
  <div class="photo-disc photo-disc--sunset" style="left:33px;top:135px;width:120px;height:120px" role="img" aria-label="Boat at dusk with green underwater lights"></div>
  <div class="photo-disc photo-disc--green" style="left:265px;top:135px;width:120px;height:120px" role="img" aria-label="Two boats with green and white hull lighting"></div>
  <div class="photo-disc photo-disc--wake" style="left:150px;top:211px;width:120px;height:120px" role="img" aria-label="Boat stern glowing blue in dark water"></div>

  <h1 class="brand-name">Cobalto Grande</h1>

  <p class="line line--web" style="left:538px;top:161px">www.hullglowtap.example</p>
  <p class="line line--email" style="left:532px;top:193px">CobaltoGrande@mailvista.example</p>
  <p class="line line--phone" style="left:543px;top:223px">555-271-0648</p>
  <p class="line line--service" style="left:481px;top:282px">Underwater <strong>LED</strong> watercraft lighting</p>
  <p class="line line--service" style="left:481px;top:320px">Boat Drain Plug lights</p>
</section>

<section class="card card--audio">
  <div class="card__backdrop" role="img" aria-label="Soft-focus showroom wall lined with speaker enclosures"></div>

  <h1 class="brand-name">Cobalto Grande</h1>

  <p class="line line--heading" style="left:214px;top:166px">SPEAKER ENCLOSURES</p>
  <p class="line line--sub" style="left:216px;top:204px">Auto, Boat and <strong>ATV</strong></p>
  <p class="line line--phone" style="left:214px;top:269px">555-271-0648</p>
  <p class="line line--email" style="left:214px;top:301px">CobaltoGrande@mailvista.example</p>
  <p class="line line--web" style="left:214px;top:333px">www.versatilesoundshells.example</p>

  <div class="photo-disc photo-disc--speaker" style="left:422px;top:77px;width:120px;height:120px" role="img" aria-label="Round speaker pod with silver grille"></div>
  <div class="photo-disc photo-disc--pod" style="left:519px;top:172px;width:120px;height:120px" role="img" aria-label="Black angled speaker enclosure"></div>
  <div class="photo-disc photo-disc--speaker" style="left:378px;top:206px;width:120px;height:120px" role="img" aria-label="Speaker pod with grille and tweeter"></div>
</section>

</body>
</html>
```